Belarde's Plumbing, Heating, and AC Buisness card

I need a business card design for my Plumbing Heating and AC company. We are based out of North Windham, CT, and offer residential and light commercial services. I am looking for something that incorporates a water droplet, snowflake, and flame. I would like it to be Modern and different from a typical business card but needs to communicate confidence and security.

```html
<!DOCTYPE html>
<html lang="en">
<head>
<meta charset="utf-8">
<title>Belarde's Plumbing, Heating, and AC – Business Card</title>
<link href="https://fonts.googleapis.com/css2?family=Roboto:wght@400;500;700;900&display=swap" rel="stylesheet">
<style>
  :root {
    --backdrop: #2c2c2c;
    --card: #efefef;
    --navy: #1d3a8a;
    --blue: #0a63a8;
    --blue-deep: #0b4f91;
    --indigo: #2a1f6e;
    --orange: #e07a12;
    --amber: #e8a90c;
    --red: #d0321b;
    --ink: #2a2a2a;
    --rule: #3a3a3a;
  }
  * { box-sizing: border-box; margin: 0; padding: 0; }
  html, body {
    width: 1200px; height: 1138px; overflow: hidden;
    background: var(--backdrop);
    font-family: "Roboto", Arial, sans-serif;
  }
  .card {
    position: absolute;
    width: 620px; height: 375px;
    background: var(--card);
    border-radius: 16px;
    overflow: hidden;
  }
  .card--front { left: 274px; top: 186px; }
  .card--back  { left: 276px; top: 608px; }

  .brand-mark {
    position: absolute;
    border-radius: 50%;
    background: var(--blue);
  }
  .brand-name {
    position: absolute;
    font-weight: 700;
    color: var(--navy);
    line-height: 1;
    white-space: nowrap;
  }
  .brand-services {
    position: absolute;
    font-weight: 900;
    color: var(--orange);
    letter-spacing: 0.26em;
    white-space: nowrap;
    line-height: 1;
  }

  /* front */
  .card--front .brand-mark { left: 266px; top: 72px; width: 90px; height: 90px; }
  .card--front .brand-name { left: 0; width: 620px; text-align: center; top: 196px; font-size: 58px; }
  .card--front .brand-services { left: 0; width: 620px; text-align: center; top: 258px; font-size: 14px; }
  .front-web {
    position: absolute; left: 0; width: 620px; top: 318px;
    display: flex; justify-content: center; align-items: center; gap: 22px;
    font-size: 16px; color: var(--ink);
  }
  .front-web .rule { width: 72px; height: 3px; background: var(--rule); border-radius: 2px; }
  .front-band { position: absolute; left: 0; bottom: 0; width: 620px; height: 16px; display: flex; }
  .front-band .cool { flex: 1; background: linear-gradient(90deg, var(--blue), var(--blue-deep)); }
  .front-band .warm { flex: 1; background: linear-gradient(90deg, var(--orange), var(--amber)); }

  /* back */
  .card--back .brand-mark { left: 38px; top: 66px; width: 88px; height: 88px; }
  .card--back .brand-name { left: 152px; top: 66px; font-size: 56px; }
  .card--back .brand-services { left: 152px; top: 126px; font-size: 14px; }

  .person { position: absolute; left: 35px; top: 210px; }
  .person__name { font-size: 23px; font-weight: 700; color: var(--blue); }
  .person__role { font-size: 16px; color: var(--ink); margin-top: 4px; }
  .address { position: absolute; left: 36px; top: 292px; font-size: 16px; line-height: 26px; color: var(--ink); }

  .contacts { position: absolute; left: 330px; top: 228px; list-style: none; }
  .contacts li { display: flex; align-items: center; height: 26px; font-size: 17px; color: var(--ink); }
  .contacts svg { width: 16px; height: 16px; margin-right: 20px; flex: none; }

  .back-strip { position: absolute; left: 0; bottom: 0; width: 300px; height: 14px;
    background: linear-gradient(90deg, var(--red), var(--orange), var(--amber)); }
  .slogan-band { position: absolute; left: 264px; bottom: 0; width: 356px; height: 47px; }
  .slogan-band svg { position: absolute; inset: 0; }
  .slogan-band span { position: absolute; left: 62px; top: 14px; font-size: 16px; color: #fff; }
</style>
</head>
<body>
  <section class="card card--front">
    <span class="brand-mark"></span>
    <div class="brand-name">BELARDE'S</div>
    <div class="brand-services">PLUMBING | HEATING | AC</div>
    <div class="front-web"><span class="rule"></span>www.belardeplumbing.com<span class="rule"></span></div>
    <div class="front-band"><span class="cool"></span><span class="warm"></span></div>
  </section>

  <section class="card card--back">
    <span class="brand-mark"></span>
    <div class="brand-name">BELARDE'S</div>
    <div class="brand-services">PLUMBING | HEATING | AC</div>

    <div class="person">
      <div class="person__name">John Doe Smith</div>
      <div class="person__role">Managing Director</div>
    </div>
    <div class="address">234 Anywhere St., Any City,<br>Any Town, US 123456</div>

    <ul class="contacts">
      <li><svg viewBox="0 0 16 16"><path d="M2 6c0-2 3-3 6-3s6 1 6 3v1h-3V5.5H5V7H2z M4 8h8l1 5H3z" fill="var(--orange)"/></svg>828-111-1111</li>
      <li><svg viewBox="0 0 16 16"><rect x="1" y="3" width="14" height="10" fill="var(--orange)"/><path d="M1 3l7 6 7-6" fill="none" stroke="#fff" stroke-width="1.4"/></svg>john@yourwebsite.com</li>
      <li><svg viewBox="0 0 16 16"><circle cx="8" cy="8" r="7" fill="var(--orange)"/><path d="M1 8h14M8 1c-3 3-3 11 0 14M8 1c3 3 3 11 0 14" fill="none" stroke="#fff" stroke-width="1"/></svg>www.yourwebsite.com</li>
    </ul>

    <div class="back-strip"></div>
    <div class="slogan-band">
      <svg viewBox="0 0 356 47" preserveAspectRatio="none">
        <defs><linearGradient id="sloganFill" x1="0" x2="1"><stop offset="0" stop-color="#0a63a8"/><stop offset="1" stop-color="#2a1f6e"/></linearGradient></defs>
        <path d="M30 0H356V47H0L22 6Q25 0 30 0Z" fill="url(#sloganFill)"/>
      </svg>
      <span>Slogan is Here</span>
    </div>
  </section>
</body>
</html>
```